Finally a Vodka produced for women ! (Label Design)

We are a small distillery based in Melbourne, Australia and we need a Vodka label design solution that will appeal to women aged 30-50 years and radiate luxury. Full Details are in a design brief attached. We thank you in advance.

Target Market(s)

Affluent females 30-50 years.

Industry/Entity Type

Spirits/Alcohol

Requirements
Must have
• Be clear this is a luxury Vodka.
Nice to have
• Elegance.

```html
<!DOCTYPE html>
<html lang="en">
<head>
<meta charset="utf-8">
<title>Silver Heron Distillery – Pink Opal Vodka Labels</title>
<link rel="stylesheet" href="https://fonts.googleapis.com/css2?family=Bodoni+Moda:wght@400;500&family=Montserrat:wght@400;500;600&family=Quicksand:wght@500;600&display=swap">
<style>
  :root {
    --page: #ffffff;
    --label-rose: #c9a0b4;
    --accent-magenta: #a1238e;
    --ink-white: #ffffff;
    --sans: "Montserrat", sans-serif;
    --serif: "Bodoni Moda", serif;
    --rounded: "Quicksand", sans-serif;
  }
  html, body {
    margin: 0;
    padding: 0;
    width: 720px;
    height: 1200px;
    overflow: hidden;
    background: var(--page);
  }
  .sheet {
    width: 720px;
    height: 1200px;
    display: flex;
    flex-direction: column;
  }
  .option {
    height: 600px;
    display: flex;
    align-items: center;
    justify-content: center;
  }
  .label {
    position: relative;
    width: 400px;
    height: 520px;
    color: var(--ink-white);
    text-align: center;
  }
  .label-shape {
    position: absolute;
    inset: 0;
    width: 400px;
    height: 520px;
  }
  .label-text {
    position: absolute;
    left: 0;
    right: 0;
    margin: 0;
  }
  .brand-name {
    top: 188px;
    font-family: var(--sans);
    font-weight: 600;
    font-size: 21px;
    letter-spacing: 6px;
    line-height: 24px;
  }
  .brand-sub {
    top: 240px;
    font-family: var(--sans);
    font-weight: 500;
    font-size: 8px;
    letter-spacing: 5px;
  }
  .spirit {
    top: 282px;
    font-family: var(--sans);
    font-weight: 400;
    font-size: 15px;
    letter-spacing: 0.5px;
  }
  .grade {
    top: 301px;
    font-family: var(--sans);
    font-weight: 400;
    font-size: 11px;
  }
  .product-name {
    top: 324px;
    font-family: var(--serif);
    font-weight: 500;
    font-size: 30px;
    letter-spacing: 0.5px;
  }
  .product-sub {
    top: 364px;
    font-family: var(--serif);
    font-size: 10px;
    letter-spacing: 9px;
  }
  .origin {
    top: 408px;
    font-family: var(--sans);
    font-size: 8px;
  }
  .volume {
    top: 448px;
    font-family: var(--serif);
    font-size: 12px;
    line-height: 15px;
  }
  /* Option two: magenta band */
  .label--band .product-name {
    top: 326px;
    font-family: var(--rounded);
    font-weight: 600;
    font-size: 28px;
    letter-spacing: 1px;
  }
  .label--band .product-sub {
    top: 360px;
    font-family: var(--sans);
    font-size: 13px;
    letter-spacing: 6px;
  }
  .label--band .volume {
    top: 450px;
    font-family: var(--sans);
    font-size: 8px;
    line-height: 14px;
  }
</style>
</head>
<body>
<main class="sheet">

  <section class="option">
    <div class="label label--classic">
      <svg class="label-shape" viewBox="0 0 400 520" aria-hidden="true">
        <polygon points="200,0 392,430 300,520 100,520 8,430" fill="var(--label-rose)"/>
      </svg>
      <p class="label-text brand-name">SILVER<br>HERON</p>
      <p class="label-text brand-sub">DISTILLERY</p>
      <p class="label-text spirit">VODKA</p>
      <p class="label-text grade">PREMIUM</p>
      <p class="label-text product-name">PINK OPAL</p>
      <p class="label-text product-sub">FILTERED</p>
      <p class="label-text origin">HANDCRAFTED IN MELBOURNE, AUSTRALIA.</p>
      <p class="label-text volume">10% ALC/VOL<br>700 ML</p>
    </div>
  </section>

  <section class="option">
    <div class="label label--band">
      <svg class="label-shape" viewBox="0 0 400 520" aria-hidden="true">
        <polygon points="200,0 392,430 300,520 100,520 8,430" fill="var(--label-rose)"/>
        <polygon points="200,22 374,420 290,500 110,500 26,420" fill="none" stroke="var(--accent-magenta)" stroke-width="3"/>
        <rect x="0" y="318" width="400" height="64" fill="var(--accent-magenta)"/>
      </svg>
      <p class="label-text brand-name">SILVER<br>HERON</p>
      <p class="label-text brand-sub">DISTILLERY</p>
      <p class="label-text spirit">VODKA</p>
      <p class="label-text grade">PREMIUM</p>
      <p class="label-text product-name">PINK OPAL</p>
      <p class="label-text product-sub">FILTERED</p>
      <p class="label-text origin">HANDCRAFTED IN MELBOURNE, AUSTRALIA.</p>
      <p class="label-text volume">10% ALC/VOL<br>700 ML</p>
    </div>
  </section>

</main>
</body>
</html>
```